Global E-commerce Business Needs Banner Ad

We need banner ads for a fast growing E-commerce business cater mostly to women. The ads must have unique and beautiful background that accentuate the products. The ads should also have between 1-4 products in it. It needs to have the headline "Up To 80% Off Retail" in the ad. The ad also needs to have our logo and a "View Now" button. The ad should be more feminine and playful. Each product should have a different background design specially for the product to make it more beautiful.

Dimension: 320 by 480 pixel

Target Market(s)

Women

Industry/Entity Type

Business

Requirements
Must have
• 1) "Up To 80% Off Retail"
• 2) Brimvale Logo
• 3) "View Now" button

```html
<!DOCTYPE html>
<html lang="en">
<head>
<meta charset="utf-8">
<title>Brimvale – Up To 80% Off Retail banners</title>
<link rel="stylesheet" href="https://fonts.googleapis.com/css2?family=Noto+Serif:ital,wght@0,400;1,400;1,700&family=Great+Vibes&display=swap">
<style>
  :root {
    --stage: #8c5c34;
    --paper: #ffffff;
    --ink: #1d1a1c;
    --cta: #0c0709;
    --cta-text: #f4eef2;
    --headline: #ffffff;
  }
  * { box-sizing: border-box; margin: 0; padding: 0; }
  html, body {
    width: 1200px;
    height: 720px;
    overflow: hidden;
    background: var(--stage);
  }
  .stage {
    position: relative;
    width: 1200px;
    height: 720px;
  }
  .banner {
    position: absolute;
    top: 150px;
    width: 256px;
    height: 382px;
    background: var(--paper);
    overflow: hidden;
    box-shadow: 0 3px 10px rgba(0, 0, 0, 0.35);
  }
  .banner--one   { left: 30px; }
  .banner--two   { left: 320px; }
  .banner--three { left: 608px; }
  .banner--four  { left: 903px; top: 146px; }

  .banner__scene {
    position: absolute;
    inset: 0;
  }
  .banner--one .banner__scene {
    background:
      radial-gradient(circle at 92% 25%, #f39cc6 0 14%, transparent 40%),
      radial-gradient(circle at 8% 78%, #ef92c2 0 14%, transparent 40%),
      linear-gradient(160deg, #c8a2cf 0%, #d9a9cf 45%, #b894c4 100%);
  }
  .banner--two .banner__scene {
    background:
      radial-gradient(ellipse at 50% 48%, #f4f4f4 0 22%, transparent 60%),
      linear-gradient(180deg, #777777 0%, #b9b9b9 40%, #8d8d8d 75%, #6a6a6a 100%);
  }
  .banner--three .banner__scene {
    background:
      radial-gradient(circle at 8% 18%, #f3a7c9 0 14%, transparent 38%),
      radial-gradient(circle at 92% 82%, #f4a9c8 0 14%, transparent 38%),
      linear-gradient(150deg, #eeaecb 0%, #f2c6d9 35%, #a6d8e2 65%, #7fc6d4 100%);
  }
  .banner--four .banner__scene {
    background:
      radial-gradient(circle at 94% 15%, #f0b0c8 0 10%, transparent 30%),
      radial-gradient(circle at 6% 82%, #e6a6c2 0 10%, transparent 30%),
      linear-gradient(165deg, #8c9ec2 0%, #c7cfe0 45%, #eef0f5 60%, #a8b4cc 100%);
  }

  .banner__product {
    position: absolute;
    top: 100px;
    left: 50%;
    transform: translateX(-50%);
    height: 200px;
    border-radius: 14px;
  }
  .banner--one .banner__product {
    width: 150px;
    background: linear-gradient(180deg, #e86fb0 0%, #2b2228 40%, #1a1418 75%, rgba(80,60,75,0.4) 100%);
  }
  .banner--two .banner__product {
    width: 140px;
    background: linear-gradient(180deg, #f7f7f7 0%, #d8d8d8 30%, #e2b865 60%, #c99a45 85%, rgba(200,200,200,0.4) 100%);
  }
  .banner--three .banner__product {
    width: 130px;
    background: linear-gradient(180deg, #d63f8c 0%, #5aa3d8 25%, #c9ccd4 55%, #e9ebef 80%, rgba(220,230,240,0.4) 100%);
  }
  .banner--four .banner__product {
    width: 230px;
    height: 180px;
    top: 110px;
    background: linear-gradient(180deg, #e0559a 0%, #2d2830 35%, #1d1a20 70%, rgba(70,70,85,0.4) 100%);
  }

  .banner__frame {
    position: absolute;
    inset: 0;
    width: 256px;
    height: 382px;
  }
  .banner__frame path { fill: var(--paper); }

  .banner__brand {
    position: absolute;
    top: 11px;
    left: 0;
    width: 100%;
    display: flex;
    align-items: center;
    justify-content: center;
    gap: 5px;
    font-family: "Noto Serif", serif;
    font-weight: 400;
    font-size: 19px;
    letter-spacing: 1px;
    color: var(--ink);
  }
  .banner__brand-mark {
    width: 13px;
    height: 13px;
    background: var(--ink);
  }

  .banner__headline {
    position: absolute;
    top: 61px;
    left: 0;
    width: 100%;
    text-align: center;
    font-family: "Noto Serif", serif;
    font-style: italic;
    font-weight: 700;
    font-size: 17.5px;
    color: var(--headline);
    text-shadow: 0 1px 3px rgba(0, 0, 0, 0.35);
  }
  .banner--one .banner__headline { font-weight: 400; }

  .banner__cta {
    position: absolute;
    left: 27px;
    top: 323px;
    width: 202px;
    height: 45px;
    display: flex;
    align-items: center;
    justify-content: center;
    background: linear-gradient(180deg, #231a1f 0%, var(--cta) 55%);
    border: 1px solid #ffffff;
    font-family: "Great Vibes", cursive;
    font-size: 31px;
    word-spacing: 10px;
    color: var(--cta-text);
    text-decoration: none;
  }
</style>
</head>
<body>
<main class="stage">

  <article class="banner banner--one">
    <div class="banner__scene" role="img" aria-label="Soft pink and lilac floral background"></div>
    <div class="banner__product" role="img" aria-label="Black ring set with a pink centre stone and rows of pink and white stones"></div>
    <svg class="banner__frame" viewBox="0 0 256 382" aria-hidden="true">
      <path d="M0 0 H256 V34 L128 47 L0 34 Z"/>
      <path d="M0 347 C70 340 170 336 256 345 V382 H0 Z"/>
    </svg>
    <div class="banner__brand"><span class="banner__brand-mark"></span>BRIMVALE</div>
    <h2 class="banner__headline">Up To 80% Off Retail</h2>
    <a class="banner__cta" href="#">View Now</a>
  </article>

  <article class="banner banner--two">
    <div class="banner__scene" role="img" aria-label="Misty grey background with sparkling branches"></div>
    <div class="banner__product" role="img" aria-label="Gold ring with pavé band and a clear solitaire"></div>
    <svg class="banner__frame" viewBox="0 0 256 382" aria-hidden="true">
      <path d="M0 0 H256 V34 L128 47 L0 34 Z"/>
      <path d="M0 347 C70 340 170 336 256 345 V382 H0 Z"/>
    </svg>
    <div class="banner__brand"><span class="banner__brand-mark"></span>BRIMVALE</div>
    <h2 class="banner__headline">Up To 80% Off Retail</h2>
    <a class="banner__cta" href="#">View Now</a>
  </article>

  <article class="banner banner--three">
    <div class="banner__scene" role="img" aria-label="Pink and turquoise floral background"></div>
    <div class="banner__product" role="img" aria-label="Silver ring with a pink centre stone flanked by blue stones"></div>
    <svg class="banner__frame" viewBox="0 0 256 382" aria-hidden="true">
      <path d="M0 0 H256 V34 L128 47 L0 34 Z"/>
      <path d="M0 347 C70 340 170 336 256 345 V382 H0 Z"/>
    </svg>
    <div class="banner__brand"><span class="banner__brand-mark"></span>BRIMVALE</div>
    <h2 class="banner__headline">Up To 80% Off Retail</h2>
    <a class="banner__cta" href="#">View Now</a>
  </article>

  <article class="banner banner--four">
    <div class="banner__scene" role="img" aria-label="Pale blue floral background with pink petals"></div>
    <div class="banner__product" role="img" aria-label="Four black and silver rings with pink and blue stones in a row"></div>
    <svg class="banner__frame" viewBox="0 0 256 382" aria-hidden="true">
      <path d="M0 0 H256 V34 L128 47 L0 34 Z"/>
      <path d="M0 347 C70 340 170 336 256 345 V382 H0 Z"/>
    </svg>
    <div class="banner__brand"><span class="banner__brand-mark"></span>BRIMVALE</div>
    <h2 class="banner__headline">Up To 80% Off Retail</h2>
    <a class="banner__cta" href="#">View Now</a>
  </article>

</main>
</body>
</html>
```